Youth Sports Banner Ad - 3x5 ft banner special!

We are looking for a full page ad (8.5x11") to advertise our banner services for Youth Sports leagues. The flyers will be handed out to teams and parents in hopes to draw their business to us for team banners.
We want to show our logo, address (4187 Verbena Ln. Paso Robles). Please include that we are offering a youth sports special price on 3x5 ft team banners for $115 (plus tax). The pricing will include 1 layout with up to 2 revisions. We would like the ad to grab the attention of the audience and ask them to "Call, Email or Stop in Today!"

Our info that needs to be on the banner includes:
email: info@markwell47.net
phone: 805-291-6583

We want to really focus on our quick turnaround as we will be producing the banners withing 1-2 business days after artwork approval.
We would like to include the banner samples if possible, and if you see fit, also include that we would like the potential customer to email us their teams name, roster, and colors to help speed up the layout process.

Target Market(s)

Parents of kids playing youth sports. The flyer is meant to increase awareness of our sign shop, while offering a great discount on banners for youth sports banners.

Font styles to use
Sans Serif

Colors

Designer to choose colors to be used in the design.

Requirements
Must have
• Our logo, $115 plus tax banner price, our business information, request to send over all team information including name, roster, and team colors.
Nice to have
• Would like to see color in the ad! If you can tie in the Kelly green from our logo, that would be great.

```html
<!DOCTYPE html>
<html lang="en">
<head>
<meta charset="utf-8">
<title>Markwell – Youth Sports Banner Special</title>
<link href="https://fonts.googleapis.com/css2?family=Poppins:ital,wght@0,300;0,400;0,600;0,700;0,800;1,600&display=swap" rel="stylesheet">
<style>
  :root{
    --kelly:#1f9a3a;
    --lime:#8cc63f;
    --lime-light:#cfe83a;
    --panel-dark:#2f9e2f;
    --red:#d9261c;
    --grey-card:#d7d7d9;
    --white:#ffffff;
    --yellow:#f4e22a;
    --orange:#f5a01a;
    --ink:#1a1a1a;
    --bg:#ececec;
  }
  *{margin:0;padding:0;box-sizing:border-box}
  html,body{width:1200px;height:1000px;overflow:hidden;background:var(--bg);font-family:"Poppins",sans-serif}
  .page{position:absolute;left:223px;top:8px;width:759px;height:982px;background:var(--white);box-shadow:0 2px 10px rgba(0,0,0,.35)}
  .layer{position:absolute;left:0;top:0}
  .brand{position:absolute;left:0;width:1200px;text-align:center;line-height:1}
  .brand-logo{top:78px}
  .brand-name{display:inline-flex;align-items:center;gap:8px;font-weight:800;font-size:30px;color:var(--kelly);letter-spacing:1px}
  .brand-mark{width:14px;height:14px;background:var(--kelly)}
  .brand-address{top:154px;font-size:8px;font-weight:600;color:var(--ink)}
  .headline{position:absolute;left:380px;width:460px;text-align:center;color:var(--white);line-height:1;white-space:nowrap;text-shadow:2px 3px 0 rgba(120,80,20,.45)}
  .kicker{top:254px;font-size:11px;font-weight:400;text-shadow:none}
  .offer{top:273px;font-size:22px;font-weight:400;letter-spacing:5px}
  .discount{top:293px;font-size:57px;font-weight:800;letter-spacing:-1px}
  .pricing{top:345px;font-size:31px;font-weight:600;letter-spacing:7px}
  .size{top:368px;font-size:110px;font-weight:800;letter-spacing:-1px}
  .banner-word{top:467px;font-size:86px;font-weight:800;letter-spacing:-1px}
  .youth{top:540px;font-size:27px;font-weight:300;text-shadow:none}
  .price-tag{position:absolute;left:624px;top:574px;width:258px;height:40px;background:linear-gradient(var(--orange),#e8890c);transform:rotate(-3deg);text-align:center;color:var(--white)}
  .price-main{font-size:14px;font-weight:700;margin-top:3px;line-height:1.2}
  .price-note{font-size:7px;font-weight:600}
  .contact{position:absolute;left:443px;width:340px;text-align:center;color:var(--white);white-space:nowrap}
  .call{top:638px;font-size:22px;font-weight:700;color:var(--yellow);line-height:1.2}
  .swoosh{position:absolute;left:530px;top:664px}
  .details{top:676px;font-size:12.5px;line-height:17px}
  .details .hl{color:var(--yellow)}
  .extras{position:absolute;left:540px;top:765px;width:140px;text-align:center;font-size:7.5px;font-weight:700;color:var(--yellow);line-height:10px}
  .footer{position:absolute;left:0;width:1200px;top:910px;text-align:center;color:var(--kelly);font-style:italic;font-weight:600;font-size:11.5px;letter-spacing:.5px;line-height:16px}
</style>
</head>
<body>
  <div class="page"></div>

  <svg class="layer" width="1200" height="1000" viewBox="0 0 1200 1000">
    <circle class="basketball" cx="360" cy="240" r="90" fill="#e8731e" role="img" aria-label="Basketball illustration"/>
    <polygon class="panel-card" points="335,210 875,190 880,790 770,805 350,810" fill="var(--grey-card)"/>
    <polygon class="panel-red" points="345,215 872,155 880,790 800,838 440,805" fill="var(--red)"/>
    <polygon class="panel-green" points="360,188 888,175 860,790 820,830 420,795" fill="var(--panel-dark)"/>
    <polygon class="panel-green-face" points="372,192 885,182 855,782 430,790" fill="var(--lime)"/>
    <polygon class="panel-stripe" points="372,192 885,182 884,212 372,225" fill="var(--lime-light)"/>
    <rect class="shuttlecock" x="765" y="140" width="150" height="135" rx="50" fill="#e6e3dc" role="img" aria-label="Badminton shuttlecock illustration"/>
    <rect class="paddles" x="245" y="470" width="135" height="150" rx="55" fill="#c9333a" role="img" aria-label="Table tennis paddles and ball illustration"/>
    <circle class="soccer-ball" cx="890" cy="700" r="72" fill="#e7e7e7" role="img" aria-label="Soccer ball illustration"/>
    <g transform="rotate(-4 378 670)">
      <rect class="sample-banner" x="272" y="605" width="210" height="128" fill="#2e2a7a" stroke="#fff" stroke-width="4" role="img" aria-label="Sample team banner with roster and mascot"/>
    </g>
    <g transform="rotate(5 818 825)">
      <rect class="sample-banner" x="707" y="755" width="222" height="140" fill="#151515" stroke="#fff" stroke-width="4" role="img" aria-label="Sample team banner in orange and black with roster"/>
    </g>
  </svg>

  <div class="brand brand-logo">
    <div class="brand-name"><span class="brand-mark"></span>MARKWELL</div>
  </div>
  <div class="brand brand-address">4187 VERBENA LN. PASO ROBLES</div>

  <div class="headline kicker">AS A LONGTIME SUPPORTER AND SPONSOR OF LOCAL SPORTS</div>
  <div class="headline offer">WE ARE OFFERING</div>
  <div class="headline discount">DISCOUNTED</div>
  <div class="headline pricing">PRICING FOR</div>
  <div class="headline size">3X5FT</div>
  <div class="headline banner-word">BANNER</div>
  <div class="headline youth">FOR LOCAL YOUTH SPORTS</div>

  <div class="price-tag">
    <div class="price-main">115$ PLUS TAX BANNER PRICE</div>
    <div class="price-note">PRICING INCLUDES 1 LAYOUT WITH UP TO 2 REVISIONS</div>
  </div>

  <div class="contact call">CALL US NOW!</div>
  <svg class="swoosh" width="180" height="10" viewBox="0 0 180 10"><path d="M2 7 Q90 0 178 5" stroke="#fff" stroke-width="2" fill="none"/></svg>
  <div class="contact details">
    <span class="hl">805-291-6583</span><br>
    or email us at <span class="hl">info@markwell47.net</span><br>
    with your teams name, roster,<br>
    and colors to help speed up the layout process.
  </div>
  <div class="extras">WE ALSO OFFER VEHICLE GRAPHICS, STOREFRONT SIGNS, SAFETY SIGNS, REFLECTIVE SIGNS AND MORE!</div>

  <div class="footer">MARKWELL PRINTING SERVICES IS PROUD TO BE A<br>LOCAL FAMILY BUSINESS THAT OFFERS A VERY FAST TURNAROUND.</div>
</body>
</html>
```